Dentistry Office

We want a new design for a Dentist's office website.

The theme is: "We provide high quality, state-of-the-art, dental care in a comfortable, caring environment."

The site currently has a menu on the left of the page with about 40 items on it. There is a great deal of textual content on each page, plus several illustrations.

We want to do this using CSS, so we need specifications in the CSS for all possible elements. The CSS needs to be named in a logical manner for easy use.

Every dentist on the planet seems to use lots of Flash. We don't want to because it is so distracting. We are looking for an elegant solution targeting 24-55 age group, but not excluding anyone.

The following (from another dentist's site) can give you a taste of what we want to communicate on the site:

"After 20 years of teaching dentists how to refine their technique and many years of writing textbooks, I currently devote my time to my office and the hands-on practice of dentistry. I'd like to welcome you personally to my dental practice, and I invite you to meet my highly experienced team of professionals.

"We have offered complete dental care of the highest quality since 1978. We provide Preventive Services, Tooth Whitening and Cosmetic Dentistry for a beautiful smile, Endodontics (root canal treatment) to treat painful teeth, Sedation Dentistry so you can relax, and Dental Implants to restore what is missing. We offer total care.

"Our approach to your health is simple: We use our education, experience and dedication to provide every patient with superior dental care.

"This passion for excellence is not just a goal, but a standard every member of our team holds.

"We also pride ourselves with our state of the art procedures, training and technology. This includes creating a beautiful smile using techniques that preserve as much of the original tooth as possible.

"Our abilities are renowned throughout the dental profession and I hope if you have any questions you will contact us by an e-mail note, by phone or just by dropping by."

Keep in mind the screen shape and dimensions. Your design needs to work in the normal screen proportions, regardless of how it looks when you post it here. Scrolling is OK, but the first impression needs to work.

Keep in mind that there will be about 250 words, or more, on each page.

Competitors web sites:

http://www.brevalkoortho.example/

http://www.quimbelfieldcare.example/

http://www.grinsatdoverellclinic.example/

http://www.trunwickfamilydentalcare.example/

http://www.morvanhaledental.example/

http://www.ubrigandental.example/

We need to compete with these.

Target Market(s)

Generally adults seeking the most experienced and comfortable-to-be-with dentist.

Industry/Entity Type

Training

Requirements
Must have
• Must stand apart from other dentists.
• Must be elegant.
• Must have a horizontal menu structure across all columns, NOT a vertical that requires scrolling, no popout, pop down, etc. menus.
• We are looking for something special.
• Do not waste your time or ours putting up templates and things you have used before.
• Personally, I do not see how someone outside the US can understand the northern California dental market. But you are welcome to try.
Should not have
• Flash or graphics that move
• The look of a template
• Folksy fonts
• Looks like you used it 20 times before

```html
<!DOCTYPE html>
<html lang="en">
<head>
<meta charset="utf-8">
<title>Dental Care</title>
<link href="https://fonts.googleapis.com/css2?family=Ubuntu:wght@400;500&family=Arimo:wght@400;700&family=Oswald:wght@400&display=swap" rel="stylesheet">
<style>
:root{
  --orange:#fdbb38;
  --orange-dark:#f6a313;
  --orange-line:#e9a21f;
  --orange-soft:#fcd37a;
  --blue:#2a8bdc;
  --blue-dark:#1d5fa3;
  --navy:#1b4f8a;
  --panel:#f7f6f4;
  --text:#222;
  --white:#fff;
}
*{margin:0;padding:0;box-sizing:border-box}
html,body{width:887px;height:1200px;overflow:hidden;background:var(--white)}
body{position:relative;font-family:"Arimo",Arial,sans-serif;color:var(--text)}
.abs{position:absolute}

.site-header{left:0;top:0;width:887px;height:92px}
.brand{left:34px;top:16px}
.brand-name{font-family:"Ubuntu",sans-serif;font-size:38px;font-weight:400;color:var(--navy);line-height:1}
.brand-tag{font-family:"Ubuntu",sans-serif;font-size:10px;font-weight:500;color:var(--orange-dark);margin-top:4px;margin-left:8px}
.header-call{right:17px;top:24px;text-align:right;font-family:"Oswald",sans-serif;line-height:1.05}
.header-call .label{font-size:22px;color:var(--orange-dark)}
.header-call .number{font-size:24px;color:var(--navy)}

.hero-band{left:0;top:92px;width:887px;height:282px;background:var(--orange)}
.hero-panel{left:16px;top:112px;width:853px;height:320px;background:var(--panel);box-shadow:0 14px 18px -8px rgba(0,0,0,.35)}

.main-nav{left:30px;top:124px;width:827px;height:42px;background:var(--orange);border:3px solid var(--orange-dark);padding:3px;z-index:3}
.main-nav ul{list-style:none;border:2px solid var(--orange-soft);height:100%;display:flex;justify-content:space-between;align-items:center;padding:0 14px}
.main-nav li{font-family:"Ubuntu",sans-serif;font-size:14px;color:var(--white);white-space:nowrap}
.main-nav li.current{color:#222}
.main-nav .sep{width:1px;height:16px;background:var(--orange-line)}

.hero-photo-left{left:150px;top:198px;width:150px;height:170px;border:6px solid var(--white);transform:rotate(-8deg);background:linear-gradient(135deg,#d6dde2,#8c9aa5 60%,#ece9e4)}
.hero-photo-right{left:596px;top:198px;width:140px;height:170px;border:6px solid var(--white);transform:rotate(6deg);background:linear-gradient(135deg,#f2f3f4,#c8cfd4 50%,#e0c6b3)}
.hero-photo-main{left:280px;top:176px;width:330px;height:186px;border:6px solid var(--white);background:linear-gradient(120deg,#dfe6ea,#9cc5dc 45%,#e3c8a8)}
.hero-banner{left:30px;top:356px;width:827px;height:59px;background:var(--blue);color:var(--white);font-family:"Ubuntu",sans-serif;font-size:19px;line-height:59px;text-align:center;white-space:nowrap;z-index:2}

.side-head{left:34px;top:467px;width:208px;height:39px;background:var(--blue);color:var(--white);font-family:"Ubuntu",sans-serif;font-size:14px;text-align:center;line-height:39px;box-shadow:0 3px 4px rgba(0,0,0,.3);z-index:2}
.side-list{left:37px;top:506px;width:202px;height:581px;background:var(--orange);border:2px solid var(--orange-soft);list-style:none;padding:4px 12px 0}
.side-list li{font-family:"Arimo",sans-serif;font-weight:700;font-size:10px;color:var(--white);height:28.3px;line-height:28px;padding-left:11px;border-bottom:1px solid var(--orange-line)}
.side-list li:last-child{border-bottom:none}

.welcome{left:261px;top:470px;width:608px;height:42px;border-bottom:1px dashed #aaa;font-family:"Ubuntu",sans-serif;font-weight:400;font-size:23px;color:#111;white-space:nowrap}
.welcome .name{font-family:"Oswald",sans-serif;font-size:30px;color:var(--orange-dark);margin-left:4px}
.intro{left:263px;top:526px;width:316px}
.intro p,.body-copy p{font-size:10.3px;line-height:15.9px;margin-bottom:16px}
.intro-photo{left:593px;top:527px;width:276px;height:184px;border:6px solid var(--white);box-shadow:0 0 4px rgba(0,0,0,.25);background:linear-gradient(120deg,#e8edf0,#aebfcc 50%,#c89c86)}
.body-copy{left:266px;top:732px;width:603px}
.rule{left:261px;top:918px;width:608px;border-top:1px dashed #aaa}

.feature{top:941px;width:190px}
.feature h3{font-family:"Ubuntu",sans-serif;font-weight:400;font-size:16px;color:var(--blue-dark);height:35px}
.feature-card{position:relative;height:111px;border:4px solid #f0f2f4;outline:1px solid #ccc;border-radius:5px;overflow:hidden}
.feature-card span{position:absolute;left:0;right:0;bottom:8px;text-align:center;font-family:"Times New Roman",serif;color:var(--white);text-shadow:0 1px 3px #000;white-space:nowrap}
.feature-call{left:261px}
.feature-call .feature-card{background:linear-gradient(135deg,#dfe6ec,#a7b6c2 60%,#6f5a4d)}
.feature-call span{font-size:28px;bottom:6px}
.feature-implants{left:471px}
.feature-implants .feature-card{background:linear-gradient(135deg,#f1eeea,#d9b2a4 55%,#b78a74)}
.feature-implants span{font-size:18px}
.feature-dentists{left:680px}
.feature-dentists .feature-card{background:linear-gradient(135deg,#f3f3f0,#cfd9e0 55%,#b5b9bc)}
.feature-dentists span{font-size:18px}

.site-footer{left:0;top:1130px;width:887px;height:70px;background:var(--blue);color:var(--white);font-family:"Ubuntu",sans-serif;font-size:9.5px;line-height:70px;text-align:center;white-space:nowrap}
.site-footer .sep{margin:0 6px}
</style>
</head>
<body>
<header class="site-header abs">
  <div class="brand abs">
    <div class="brand-name">Dental Care</div>
    <div class="brand-tag">The Best Dental Care of Northern California</div>
  </div>
  <div class="header-call abs"><div class="label">Call Us</div><div class="number">555.0142.7788</div></div>
</header>

<div class="hero-band abs"></div>
<div class="hero-panel abs"></div>
<nav class="main-nav abs">
  <ul>
    <li class="current">Home</li><li class="sep"></li><li>About Us</li><li class="sep"></li><li>Our Practice</li><li class="sep"></li><li>Procedures</li><li class="sep"></li><li>Our Mission</li><li class="sep"></li><li>Dental Implants</li><li class="sep"></li><li>FAQs</li><li class="sep"></li><li>Smile Gallery</li><li class="sep"></li><li>Contact Us</li>
  </ul>
</nav>
<div class="hero-photo-left abs" role="img" aria-label="Dental assistant at work in the treatment room"></div>
<div class="hero-photo-right abs" role="img" aria-label="Patient relaxing in the dental chair"></div>
<div class="hero-photo-main abs" role="img" aria-label="Smiling hygienist showing dental floss to a patient"></div>
<div class="hero-banner abs">High quality Dental Care in A Comfortable, Caring Environment</div>

<div class="side-head abs">Left Panel</div>
<ul class="side-list abs">
  <li>lorem ipsum dolor sit amet</li><li>lorem ipsum dolor sit amet</li><li>lorem ipsum dolor sit amet</li><li>lorem ipsum dolor sit amet</li><li>lorem ipsum dolor sit amet</li><li>lorem ipsum dolor sit amet</li><li>lorem ipsum dolor sit amet</li><li>lorem ipsum dolor sit amet</li><li>lorem ipsum dolor sit amet</li><li>lorem ipsum dolor sit amet</li><li>lorem ipsum dolor sit amet</li><li>lorem ipsum dolor sit amet</li><li>lorem ipsum dolor sit amet</li><li>lorem ipsum dolor sit amet</li><li>lorem ipsum dolor sit amet</li><li>lorem ipsum dolor sit amet</li><li>lorem ipsum dolor sit amet</li><li>lorem ipsum dolor sit amet</li><li>lorem ipsum dolor sit amet</li><li>lorem ipsum dolor sit amet</li>
</ul>

<h1 class="welcome abs">welcome to <span class="name">Dental Care</span></h1>
<div class="intro abs">
  <p>"After 20 years of teaching dentists how to refine their technique and many years of writing textbooks, I currently devote my time to my office and the hands-on practice of dentistry. I'd like to welcome you personally to my dental practice, and I invite you to meet my highly experienced team of professionals.</p>
  <p>"We have offered complete dental care of the highest quality since 1978. We provide Preventive Services, Tooth Whitening and Cosmetic Dentistry for a beautiful smile, Endodontics (root canal treatment) to treat painful teeth, Sedation Dentistry so you can relax, and Dental Implants to restore what is missing. We offer total care.</p>
</div>
<div class="intro-photo abs" role="img" aria-label="Dentist talking with a patient in the treatment chair"></div>
<div class="body-copy abs">
  <p>"Our approach to your health is simple: We use our education, experience and dedication to provide every patient with superior dental care.</p>
  <p>"This passion for excellence is not just a goal, but a standard every member of our team holds.</p>
  <p>"We also pride ourselves with our state of the art procedures, training and technology. This includes creating a beautiful smile using techniques that preserve as much of the original tooth as possible.</p>
  <p>"Our abilities are renowned throughout the dental profession and I hope if you have any questions you will contact us by an e-mail note, by phone or just by dropping by."</p>
</div>
<div class="rule abs"></div>

<section class="feature feature-call abs">
  <h3>Call Us</h3>
  <div class="feature-card" role="img" aria-label="Woman on the phone"><span>555.018.2046</span></div>
</section>
<section class="feature feature-implants abs">
  <h3>Dental Implants</h3>
  <div class="feature-card" role="img" aria-label="Dental model of teeth">
    <span>More Information
      <svg width="22" height="22" viewBox="0 0 22 22" style="vertical-align:-5px"><circle cx="11" cy="11" r="10" fill="#222" stroke="#fff" stroke-width="1.5"/><path d="M6 11h9M11 7l4 4-4 4" stroke="#fff" stroke-width="2" fill="none"/></svg>
    </span>
  </div>
</section>
<section class="feature feature-dentists abs">
  <h3>Meet The Dentists</h3>
  <div class="feature-card" role="img" aria-label="Members of the dental team"><span>View List of Dentists</span></div>
</section>

<footer class="site-footer abs">
  © Copyright Dental Care<span class="sep">|</span>All Rights Reserved&nbsp;&nbsp;Home<span class="sep">|</span>About Us<span class="sep">|</span>Our Practice<span class="sep">|</span>Procedures<span class="sep">|</span>Our Mission<span class="sep">|</span>Dental Implants<span class="sep">|</span>FAQs<span class="sep">|</span>Smile Gallery<span class="sep">|</span>Contact Us
</footer>
</body>
</html>
```